Design the Marketing Brochure for a service company with Zenith 500 Clients

We need to redesign our marketing brochures to reflect the new service lines we have added in the last few years. We are a professional staffing firm based in Miami, Florida and have a portfolio of clients that include: Velmora Seaways, Tidewell Voyage Lines, Grillano Foods Corp, Horizon Lens Network Etc. I have attached our current marketing inserts in pdf format. I would like to have 5 inserts displaying our services, process and business lines.

Target Market(s)

Zenith 1000 companies. Within those companies our clients are: CFO's, VP of Finance, Controller, Head of Human Resources, Banking Executives etc. All financial related roles.

Industry/Entity Type

Recruitment

Colors
ec1f27
ffffff
aaaaaa
fece3e
000000

Requirements
Must have
• 5 pages 3 of which we have mots of the content. One page dedicated to " Temporary Staffing" and one page dedicated to our "Banking Division" The brochures should include professional pictures and a well designed layout that looks professional and appealing to an educated client. Our colors are Red, Gray and White.
• Please see our attached brochures and our website at www.kvtrecruit.example
Nice to have
• Professional pictures of people in the business workplace.
Should not have
• Graphics or cartoons of any kind.

```html
<!DOCTYPE html>
<html lang="en">
<head>
<meta charset="utf-8">
<title>Temporary Staffing – KVT International</title>
<link rel="stylesheet" href="https://fonts.googleapis.com/css2?family=Barlow:wght@500;700&family=Roboto+Condensed:wght@300&display=swap">
<style>
  :root {
    --red: #ec1f27;
    --black: #000000;
    --white: #ffffff;
    --gray: #aaaaaa;
    --ink: #111111;
    --body: #555555;
    --photo-top: #d9dde2;
    --photo-bottom: #9a7c62;
  }
  * { margin: 0; padding: 0; box-sizing: border-box; }
  html, body { width: 927px; height: 1200px; overflow: hidden; background: var(--white); }
  .page { position: relative; width: 927px; height: 1200px; overflow: hidden; background: var(--white); }
  .artwork { position: absolute; inset: 0; }
  .title-block {
    position: absolute; left: 34px; top: 0; width: 283px; height: 130px;
    display: flex; align-items: center; justify-content: center;
    color: var(--white); font-family: "Barlow", sans-serif; font-weight: 700;
    font-size: 44px; line-height: 42px; text-align: center; letter-spacing: 0.5px;
    padding-top: 8px;
  }
  .content { position: absolute; left: 376px; top: 172px; width: 520px; }
  .section-heading {
    font-family: "Barlow", sans-serif; font-weight: 500; color: var(--ink);
    font-size: 30px; line-height: 34px;
  }
  .body-copy {
    font-family: "Roboto Condensed", sans-serif; font-weight: 300; color: var(--body);
    font-size: 20px; line-height: 25.5px;
  }
  .body-copy + .body-copy { margin-top: 6px; }
  .solutions { margin-bottom: 38px; }
  .temporary { margin-bottom: 44px; }
  .temp-to-hire { margin-bottom: 58px; }
  .specialties { margin-top: 0; }
  .specialty-list {
    list-style: none; display: grid; grid-template-columns: 205px 205px;
    grid-auto-flow: column; grid-template-rows: repeat(8, 25px); margin-top: 19px;
  }
  .specialty-list li::before { content: "• "; }
</style>
</head>
<body>
<div class="page">
  <svg class="artwork" width="927" height="1200" viewBox="0 0 927 1200" aria-hidden="false">
    <defs>
      <linearGradient id="photoTone" x1="0" y1="0" x2="0" y2="1">
        <stop offset="0" stop-color="#e4e7ea"/>
        <stop offset="0.5" stop-color="#c8c2ba"/>
        <stop offset="1" stop-color="#a8896e"/>
      </linearGradient>
    </defs>
    <polygon role="img" aria-label="Overhead photo of professionals working on laptops at a shared desk"
      points="34,290 318,200 318,1200 34,1200" fill="url(#photoTone)"/>
    <rect class="title-bg" x="34" y="0" width="283" height="145" fill="var(--black)"/>
    <polygon points="34,145 317,122 317,128 150,145" fill="var(--red)"/>
    <polygon points="34,145 150,145 317,128 317,124 34,140" fill="#444"/>
    <polygon class="corner-red" points="370,1037 592,1037 470,1200 250,1200" fill="var(--red)"/>
    <polygon class="corner-black" points="620,985 927,985 927,1200 505,1200" fill="var(--black)"/>
  </svg>

  <h1 class="title-block">TEMPORARY<br>STAFFING</h1>

  <main class="content">
    <section class="solutions">
      <h2 class="section-heading">Flexible Accounting Staffing Solutions</h2>
      <p class="body-copy">You can hire highly skilled professionals from KVT International in three different ways:</p>
    </section>

    <section class="temporary">
      <h2 class="section-heading">Temporary:</h2>
      <p class="body-copy">Supplement your full-time staff on a project basis. This staffing solution is effective when ongoing productivity and cost management are essential.</p>
    </section>

    <section class="temp-to-hire">
      <h2 class="section-heading">Temporary-to-hire:</h2>
      <p class="body-copy">Quickly staff a vacant position with the option to hire full time. This staffing solution is effective when you want to assess fit before you make a hiring decision.</p>
      <p class="body-copy">Staffing support for long-term projects. This staffing solution is effective for long-term or recurring projects that require a specialized skill set.</p>
    </section>

    <section class="specialties">
      <h2 class="section-heading">Areas of Accounting Staffing Expertise</h2>
      <p class="body-copy">Here are just a few of our specialty areas:</p>
      <ul class="specialty-list body-copy">
        <li>Accounting Clerk</li>
        <li>Accounting Manager</li>
        <li>Accounts Payable</li>
        <li>Accounts Receivable</li>
        <li>Auditor</li>
        <li>Billing</li>
        <li>Bookkeeping</li>
        <li>Cost Accounting</li>
        <li>Credit &amp; Collections</li>
        <li>Data Entry Clerk</li>
        <li>Financial Analyst</li>
        <li>Financial Services</li>
        <li>Payroll</li>
        <li>Senior Accountant</li>
        <li>Staff Accountant</li>
        <li>Tax Accounting</li>
      </ul>
    </section>
  </main>
</div>
</body>
</html>
```